Experienced Handyman needs a business card design

Need a business card design for a one-person Handyman business. This will be my second job (part-time) after retiring from a hands-on 30-year career. I'm experienced, a hard worker, friendly, and do quality work. Everybody needs a handman they can rely on! I've worked with wood and home renovations for 20 years on the side. I'm interested in small, quick jobs - not big renovations, or building decks or garages - more like home maintenance, installing sinks, - things like that.
Walter The Fixer LLC
Small Jobs Done Right
I'm wondering if the P or H could be made out of tools in my logo...?
Target Market(s)
Homeowners - small jobs
Industry/Entity Type
Handyman / Construction
Contact Information for Business Card
Business name & tagline (see description)...email (Walter@WalterTheFixerpro.example)...phone (555) 417-8862
Look and feel

```html
<!DOCTYPE html>
<html lang="en">
<head>
<meta charset="UTF-8">
<title>Walter The Fixer LLC — Business Card</title>
<link rel="stylesheet" href="https://fonts.googleapis.com/css2?family=Montserrat:wght@400;600;700&display=swap">
<style>
  :root {
    --page: #eef0f1;
    --card-blue: #1656a8;
    --pattern-blue: #2a63ad;
    --accent-yellow: #f6b81c;
    --ink-white: #ffffff;
  }
  * { margin: 0; padding: 0; box-sizing: border-box; }
  html, body { width: 1200px; height: 1200px; overflow: hidden; }
  body {
    background: var(--page);
    font-family: "Montserrat", Arial, sans-serif;
    position: relative;
  }
  .card {
    position: absolute;
    left: 150px;
    width: 900px;
    height: 514px;
    background: var(--card-blue);
    overflow: hidden;
    box-shadow: 0 12px 30px rgba(0,0,0,0.18);
  }
  .card--front { top: 50px; }
  .card--back { top: 636px; }

  .tool-pattern {
    position: absolute;
    inset: 0;
    background: radial-gradient(ellipse at 60% 45%, var(--pattern-blue) 0%, var(--card-blue) 80%);
  }
  .corner-glow {
    position: absolute;
    inset: 0;
    background:
      linear-gradient(200deg, var(--accent-yellow) 0%, rgba(246,184,28,0.35) 10%, rgba(22,86,168,0) 26%),
      linear-gradient(20deg, var(--accent-yellow) 0%, rgba(246,184,28,0.35) 10%, rgba(22,86,168,0) 26%);
  }

  .brand {
    position: absolute;
    display: flex;
    align-items: center;
    gap: 22px;
  }
  .brand__dot {
    width: 82px;
    height: 82px;
    border-radius: 50%;
    background: var(--accent-yellow);
    flex: none;
  }
  .brand__name {
    color: var(--ink-white);
    font-weight: 700;
    font-size: 36px;
    line-height: 1.05;
    text-transform: uppercase;
    letter-spacing: 0.5px;
  }
  .brand__tagline {
    color: var(--accent-yellow);
    font-weight: 400;
    font-size: 25px;
    text-transform: uppercase;
    letter-spacing: 1px;
    margin-top: 6px;
  }
  .card--front .brand { left: 200px; top: 190px; }
  .card--back .brand { left: 60px; top: 150px; }

  .back-art { position: absolute; inset: 0; }

  .website {
    position: absolute;
    right: 50px;
    top: 305px;
    color: var(--ink-white);
    font-weight: 600;
    font-size: 20px;
    letter-spacing: 1.5px;
    text-transform: uppercase;
    white-space: nowrap;
  }
  .divider {
    position: absolute;
    left: 160px;
    top: 285px;
    width: 4px;
    height: 115px;
    background: var(--ink-white);
  }
  .contact {
    position: absolute;
    left: 60px;
    top: 410px;
    display: grid;
    grid-template-columns: auto auto;
    column-gap: 12px;
    row-gap: 6px;
    align-items: baseline;
  }
  .contact__label {
    color: var(--accent-yellow);
    font-weight: 700;
    font-size: 30px;
    text-transform: uppercase;
    white-space: nowrap;
  }
  .contact__value {
    color: var(--ink-white);
    font-weight: 600;
    font-size: 22px;
    letter-spacing: 1px;
    white-space: nowrap;
  }
</style>
</head>
<body>

  <section class="card card--front" aria-label="Business card front">
    <div class="tool-pattern" role="img" aria-label="Faint repeating pattern of handyman tool icons"></div>
    <div class="corner-glow"></div>
    <div class="brand">
      <span class="brand__dot"></span>
      <div>
        <div class="brand__name">Walter<br>The Fixer LLC</div>
        <div class="brand__tagline">Small Jobs Done Right</div>
      </div>
    </div>
  </section>

  <section class="card card--back" aria-label="Business card back">
    <svg class="back-art" width="900" height="514" viewBox="0 0 900 514">
      <path d="M420 0 L900 0 L900 170 Q660 70 420 0 Z" fill="#2a63ad" role="img" aria-label="Faint repeating pattern of handyman tool icons"/>
      <path d="M420 0 Q660 70 900 170" fill="none" stroke="#f6b81c" stroke-width="9"/>
    </svg>
    <div class="brand">
      <span class="brand__dot"></span>
      <div>
        <div class="brand__name">Walter<br>The Fixer LLC</div>
        <div class="brand__tagline">Small Jobs Done Right</div>
      </div>
    </div>
    <div class="website">WalterTheFixerpro.example</div>
    <div class="divider"></div>
    <div class="contact">
      <span class="contact__label">Email :</span>
      <span class="contact__value">WALTER@WALTERTHEFIXERPRO.EXAMPLE</span>
      <span class="contact__label">Phone :</span>
      <span class="contact__value">(555) 417-8862</span>
    </div>
  </section>

</body>
</html>
```